New business card design to go with our new logo

just want an eye-catching business card to go with our new logo. We are open to double sided or single sided. Just want it to have the following info on it. Whatever layout you think looks best.

First and Last Name
Title
Phone 801-555-7392
Address 214 W. Cedar Lane Pleasant Grove UT 84062
Email thecrew@marloweskennelandtreat.example

```html
<!DOCTYPE html>
<html lang="en">
<head>
<meta charset="utf-8">
<title>Marlowe's Kennel &amp; Treat – Business Card</title>
<link href="https://fonts.googleapis.com/css2?family=Roboto:wght@400;700&display=swap" rel="stylesheet">
<style>
  :root {
    --sky: #2fa5d8;
    --sky-deep: #2b9fd3;
    --tangerine: #f48c4c;
    --paper: #ffffff;
    --stage: #222325;
  }
  * { box-sizing: border-box; margin: 0; padding: 0; }
  html, body {
    width: 1189px;
    height: 1200px;
    overflow: hidden;
    background: var(--stage);
    font-family: "Roboto", Arial, sans-serif;
  }
  .card {
    position: absolute;
    left: 166px;
    width: 856px;
    height: 490px;
    overflow: hidden;
    box-shadow: 0 6px 18px rgba(0,0,0,.45);
  }
  .card--front { top: 66px; background: var(--sky); }
  .card--back { top: 625px; background: var(--paper); }

  .brand {
    position: absolute;
    display: flex;
    flex-direction: column;
    align-items: center;
    font-weight: 700;
    letter-spacing: .02em;
    line-height: 1.05;
  }
  .brand__name { font-size: 50px; }
  .brand__sub { font-size: 22px; }

  .card--front .brand {
    left: 0; right: 0; top: 185px;
    color: var(--paper);
  }
  .card--back .brand {
    left: 52px; top: 185px;
    color: var(--tangerine);
  }

  .swoosh { position: absolute; inset: 0; width: 100%; height: 100%; }

  .contact {
    position: absolute;
    right: 38px;
    top: 250px;
    text-align: right;
    color: var(--paper);
    font-size: 21px;
    line-height: 1.25;
  }
  .contact__name { font-weight: 700; font-size: 28px; line-height: 1; }
  .contact__title { font-size: 21px; line-height: 1; margin-bottom: 40px; }
  .contact__address { margin-bottom: 20px; }
  .contact__line {
    display: flex;
    justify-content: flex-end;
    align-items: center;
    gap: 10px;
    height: 29px;
  }
  .icon { width: 25px; height: 25px; flex: none; }
</style>
</head>
<body>

<section class="card card--front" aria-label="Card front">
  <div class="brand">
    <span class="brand__name">MARLOWE'S</span>
    <span class="brand__sub">KENNEL &amp; TREAT</span>
  </div>
</section>

<section class="card card--back" aria-label="Card back">
  <svg class="swoosh" viewBox="0 0 1049 600" preserveAspectRatio="none" aria-hidden="true">
    <path fill="var(--tangerine)" d="M0,430 C400,432 700,340 905,226 C700,375 360,505 0,535 Z"/>
    <path fill="var(--sky-deep)" stroke="var(--paper)" stroke-width="5"
          d="M1052,36 C850,230 480,490 -5,542 L-5,605 L1052,605 Z"/>
  </svg>

  <div class="brand">
    <span class="brand__name">MARLOWE'S</span>
    <span class="brand__sub">KENNEL &amp; TREAT</span>
  </div>

  <div class="contact">
    <p class="contact__name">JORDAN HALE</p>
    <p class="contact__title">Founder</p>
    <p class="contact__address">214 W. Cedar Lane<br>Pleasant Grove UT 84062</p>
    <p class="contact__line">801-555-7392
      <svg class="icon" viewBox="0 0 24 24" aria-hidden="true">
        <circle cx="12" cy="12" r="10.5" fill="none" stroke="#fff" stroke-width="1.6"/>
        <path fill="#fff" d="M6.5 10.5c0-2 2.5-3 5.5-3s5.5 1 5.5 3l-1.8.4-.6-1.6c-1.9-.6-4.3-.6-6.2 0l-.6 1.6zM8.5 12h7l1 4h-9z"/>
      </svg>
    </p>
    <p class="contact__line">thecrew@marloweskennelandtreat.example
      <svg class="icon" viewBox="0 0 24 24" aria-hidden="true">
        <circle cx="12" cy="12" r="10.5" fill="none" stroke="#fff" stroke-width="1.6"/>
        <rect x="6.5" y="8" width="11" height="8" fill="none" stroke="#fff" stroke-width="1.4"/>
        <path d="M6.5 8l5.5 4.5L17.5 8M6.5 16l4-4M17.5 16l-4-4" fill="none" stroke="#fff" stroke-width="1.2"/>
      </svg>
    </p>
  </div>
</section>

</body>
</html>
```